New Graphic Design Project*

We would like to design a 12ft x 6 ft wallpaper for a room where deprived teen children will study at a charity. Our idea is to create a motivational wallpaper with "hands and heart" "The power is in your hands" artwork in the center (PSD attached) and with our superhero incorporated in the design. Maybe sky blue and clouds white will be a good background but you can decide best. The other walls are painted darker blue.
We are thinking maybe different inspiring words scattered around would be successful so kids can look at it in a spur- to feel motivated and also protected by the superhero.
I know that true designers will get the idea.

Files here:
https://www.filvarobox.com/sh/3kq7tpwmzxhd2b4/BBRTkyuHbzqnXX11LmvdPwQcF?dl=0

Target Market(s)

charity/teen children

```html
<!DOCTYPE html>
<html lang="en">
<head>
<meta charset="utf-8">
<title>The Power Is In Your Hands – Wallpaper</title>
<link rel="stylesheet" href="https://fonts.googleapis.com/css2?family=Black+Ops+One&family=Bangers&family=Dancing+Script:wght@600&family=Special+Elite&family=Josefin+Sans:wght@300&family=Architects+Daughter&family=Playball&family=Alfa+Slab+One&display=swap">
<style>
  :root {
    --sky-deep: #5f86d6;
    --sky-mid: #8fb0ea;
    --sky-light: #d6e3f8;
    --cloud: #ffffff;
    --ink-navy: #1f2f63;
    --ink-blue: #1d4fc4;
    --ink-dark: #26324a;
    --gold: #f3b51c;
    --orange: #f39a1a;
    --hero-violet: #4a3f8f;
    --hero-gold: #f2b423;
    --hands-slate: #4d5d7e;
    --slogan: #f4f7ff;
  }
  * { margin: 0; padding: 0; box-sizing: border-box; }
  html, body { width: 1200px; height: 600px; overflow: hidden; background: var(--sky-mid); }

  .wallpaper { position: relative; width: 1200px; height: 600px; overflow: hidden; }

  .sky {
    position: absolute; inset: 0;
    background:
      radial-gradient(ellipse 260px 140px at 1080px 130px, rgba(255,255,255,.75), transparent 70%),
      radial-gradient(ellipse 300px 160px at 930px 330px, rgba(255,255,255,.7), transparent 70%),
      radial-gradient(ellipse 340px 120px at 1050px 540px, rgba(255,255,255,.6), transparent 70%),
      radial-gradient(ellipse 260px 180px at 300px 80px, rgba(255,255,255,.55), transparent 70%),
      radial-gradient(ellipse 320px 160px at 200px 540px, rgba(255,255,255,.6), transparent 70%),
      radial-gradient(ellipse 420px 200px at 600px 560px, rgba(235,242,255,.55), transparent 70%),
      linear-gradient(180deg, var(--sky-deep) 0%, var(--sky-mid) 45%, var(--sky-light) 100%);
  }

  .light-streaks { position: absolute; left: 0; top: 0; width: 520px; height: 600px; }

  .horizon-glow {
    position: absolute; left: 0; top: 277px; width: 1200px; height: 16px;
    background: radial-gradient(ellipse 420px 8px at 600px 8px, rgba(255,255,255,.95), rgba(200,225,255,.35) 55%, transparent 100%);
  }

  .cloud-heart { position: absolute; left: 404px; top: 34px; width: 372px; height: 340px; filter: blur(2px); }

  .hands {
    position: absolute; left: 515px; top: 168px; width: 180px; height: 212px;
    border-radius: 45% 45% 30% 30%;
    background: radial-gradient(ellipse 90px 106px at 90px 100px, rgba(77,93,126,.75), rgba(77,93,126,.4) 60%, transparent 100%);
  }

  .charity-mark {
    position: absolute; left: 562px; top: 270px;
    display: flex; align-items: center; gap: 4px;
    font-family: "Josefin Sans", sans-serif; font-weight: 300;
    font-size: 13px; color: #ffffff; letter-spacing: .5px;
  }
  .charity-mark .dot { width: 8px; height: 8px; border-radius: 50%; background: #e23b4b; }

  .slogan {
    position: absolute; left: 400px; top: 390px; width: 380px;
    text-align: center;
    font-family: "Black Ops One", sans-serif; font-weight: 400;
    color: var(--slogan);
    text-shadow: 0 2px 6px rgba(40,70,140,.35);
  }
  .slogan span { display: block; }
  .slogan .line-the   { font-size: 54px; letter-spacing: 16px; line-height: 52px; }
  .slogan .line-power { font-size: 40px; letter-spacing: 10px; line-height: 38px; }
  .slogan .line-is    { font-size: 33px; letter-spacing: 6px;  line-height: 34px; }
  .slogan .line-hands { font-size: 54px; letter-spacing: 8px;  line-height: 52px; }

  .hero {
    position: absolute; left: 70px; top: 122px; width: 290px; height: 290px;
    border-radius: 40%;
    background: radial-gradient(ellipse 140px 140px at 145px 140px, var(--hero-violet), rgba(74,63,143,.6) 55%, rgba(242,180,35,.35) 82%, transparent 100%);
  }

  .hero-name {
    position: absolute; left: 104px; top: 404px;
    display: flex; align-items: center; gap: 6px;
    font-family: "Bangers", sans-serif; font-size: 46px;
    color: var(--hero-gold); letter-spacing: 2px;
    transform: rotate(-8deg);
  }
  .hero-name .mark { width: 12px; height: 12px; border-radius: 50%; background: var(--hero-gold); }

  .word { position: absolute; white-space: nowrap; }

  .w-always {
    left: 26px; top: 34px;
    font-family: "Alfa Slab One", serif; font-size: 20px; color: var(--ink-blue);
    transform: rotate(27deg); transform-origin: left center;
  }
  .w-love {
    left: 204px; top: 22px; padding: 0 8px;
    background: #ffffff; box-shadow: 1px 2px 4px rgba(0,0,0,.2);
    font-family: "Special Elite", monospace; font-size: 42px; color: var(--ink-dark);
    line-height: 46px; transform: rotate(-3deg);
  }
  .w-never {
    left: 362px; top: 128px;
    font-family: "Playball", cursive; font-size: 24px; color: var(--ink-dark);
    transform: rotate(-48deg); transform-origin: left center;
  }
  .w-hands-heart {
    left: 6px; top: 488px;
    font-family: "Dancing Script", cursive; font-size: 34px; color: #ffffff;
    text-shadow: 0 1px 3px rgba(40,60,110,.5);
    transform: rotate(12deg); transform-origin: left center;
  }
  .w-wisdom {
    left: 364px; top: 412px;
    font-family: "Architects Daughter", cursive; font-size: 20px; color: var(--ink-dark);
    transform: rotate(-6deg);
  }
  .w-strong {
    left: 262px; top: 530px;
    font-family: "Josefin Sans", sans-serif; font-weight: 300; font-size: 34px; color: var(--ink-dark);
    letter-spacing: 2px; transform: rotate(-12deg);
  }
  .w-power {
    left: 842px; top: 18px;
    font-family: "Josefin Sans", sans-serif; font-weight: 300; font-size: 54px; color: #1c1f2c;
    letter-spacing: 10px; transform: rotate(10deg); transform-origin: left top;
  }
  .w-believe {
    left: 1086px; top: 14px; padding: 0 6px;
    background: #ffffff;
    font-family: "Bangers", sans-serif; font-size: 30px; color: var(--gold);
    letter-spacing: 1px; transform: rotate(3deg);
  }
  .w-feel {
    left: 786px; top: 236px;
    font-family: "Special Elite", monospace; font-size: 40px; color: #ffffff;
    text-shadow: 1px 1px 0 #5b6d96, 0 2px 6px rgba(30,50,100,.35);
    transform: rotate(-13deg); transform-origin: left center;
  }
  .w-strength {
    left: 1030px; top: 346px;
    font-family: "Architects Daughter", cursive; font-size: 30px; color: var(--gold);
    text-shadow: 1px 1px 0 #5a4a20;
    transform: rotate(8deg);
  }
  .w-achieve {
    left: 778px; top: 372px;
    font-family: "Bangers", sans-serif; font-size: 48px; color: var(--orange);
    letter-spacing: 1px;
    text-shadow: 0 2px 4px rgba(120,70,0,.3);
    transform: rotate(-10deg);
  }
  .w-dream {
    left: 990px; top: 456px;
    font-family: "Alfa Slab One", serif; font-size: 28px; color: #2e3a58;
    text-shadow: 1px 1px 0 #ffffff;
    transform: rotate(14deg); transform-origin: left center;
  }
  .w-hope {
    left: 812px; top: 506px;
    font-family: "Alfa Slab One", serif; font-size: 40px; color: #4c5f8c;
    text-shadow: -1px -1px 0 #fff, 1px 1px 0 #fff;
    transform: rotate(-4deg);
  }
</style>
</head>
<body>
<main class="wallpaper">

  <div class="sky" role="img" aria-label="Blue sky with soft white clouds"></div>

  <svg class="light-streaks" viewBox="0 0 520 600" aria-hidden="true">
    <defs>
      <linearGradient id="streak" x1="0" y1="1" x2="1" y2="0">
        <stop offset="0" stop-color="#ffffff" stop-opacity="0"/>
        <stop offset=".5" stop-color="#ffffff" stop-opacity=".85"/>
        <stop offset="1" stop-color="#bfe0ff" stop-opacity="0"/>
      </linearGradient>
    </defs>
    <polygon points="0,250 360,120 370,130 0,290" fill="url(#streak)" opacity=".6"/>
    <polygon points="0,330 340,210 350,222 0,350" fill="url(#streak)" opacity=".5"/>
    <polygon points="0,400 320,300 330,310 0,420" fill="url(#streak)" opacity=".45"/>
    <polygon points="0,200 300,90 305,96 0,215" fill="url(#streak)" opacity=".4"/>
  </svg>

  <div class="horizon-glow" aria-hidden="true"></div>

  <svg class="cloud-heart" viewBox="0 0 306 284" preserveAspectRatio="none" role="img" aria-label="Heart shaped white cloud">
    <defs>
      <radialGradient id="cloudFill" cx=".45" cy=".35" r=".7">
        <stop offset="0" stop-color="#ffffff"/>
        <stop offset=".7" stop-color="#e3eaf8"/>
        <stop offset="1" stop-color="#bccbe8"/>
      </radialGradient>
    </defs>
    <path d="M153 270 C 70 210 8 150 8 88 C 8 40 44 8 88 8 C 120 8 143 28 153 52 C 163 28 186 8 218 8 C 262 8 298 40 298 88 C 298 150 236 210 153 270 Z" fill="url(#cloudFill)" opacity=".85"/>
  </svg>

  <div class="hands" role="img" aria-label="Illustration of two open hands cupped together, holding a heart"></div>

  <div class="charity-mark"><span class="dot"></span>Kindhold</div>

  <h1 class="slogan">
    <span class="line-the">THE</span>
    <span class="line-power">POWER</span>
    <span class="line-is">IS IN YOUR</span>
    <span class="line-hands">HANDS</span>
  </h1>

  <div class="hero" role="img" aria-label="Illustration of a superhero in a purple and gold costume running forward"></div>

  <div class="hero-name"><span class="mark"></span>SKYVOLT</div>

  <p class="word w-always">Always there for you</p>
  <p class="word w-love">love</p>
  <p class="word w-never">never alone</p>
  <p class="word w-hands-heart">hands and heart</p>
  <p class="word w-wisdom">wisdom</p>
  <p class="word w-strong">strong</p>

  <p class="word w-power">POWER</p>
  <p class="word w-believe">Believe</p>
  <p class="word w-feel">feel the power</p>
  <p class="word w-strength">strength</p>
  <p class="word w-achieve">Achieve</p>
  <p class="word w-dream">DREAM ON</p>
  <p class="word w-hope">HoPe</p>

</main>
</body>
</html>
```